Vora Leave In Conditioning Mist

The product is a 10oz light detangler in a continuous mister bottle. Trying to be an alternative to a competitor, "Brisk Lane Tidal Mist" https://brisklanehair.com/products/tidal-mist-leave-in-conditioner

The brand name is "Vora" or "VORA".
Product is a "10 in 1 Multi-Use Leave In Conditioner (lane mist)"
Featured ingredient is "Biotin" and "Keratin"

The art attached shows my attempt but it needs to be classier.

Label size is 6.75"W x 5.25"H (rounded edges).
Material is silver foil with matte finish overlay.

Thank you,
Theo

Vora

```html
<!DOCTYPE html>
<html lang="en">
<head>
<meta charset="utf-8">
<title>Vora Leave In Conditioning Mist – Labels</title>
<link rel="stylesheet" href="https://fonts.googleapis.com/css2?family=Montserrat:wght@300;700&family=Oswald:wght@300;400;500&family=Quicksand:wght@500;600&display=swap">
<style>
  :root {
    --page: #ffffff;
    --gold-dark: #d1ad86;
    --gold-light: #f1dfc8;
    --gold-dot: #e8caa4;
    --blue-top: #6b95c8;
    --blue-bottom: #73a4db;
    --blue-ink: #26318a;
    --blue-tint: #8fb3df;
    --pink-top: #dc97bd;
    --pink-bottom: #eaa7cb;
    --pink-ink: #7b1026;
    --pink-tint: #eab7d2;
    --white: #ffffff;
  }
  * { box-sizing: border-box; margin: 0; padding: 0; }
  html, body {
    width: 1070px; height: 1200px; overflow: hidden;
    background: var(--page);
  }
  .canvas { position: relative; width: 1070px; height: 1200px; }

  .label {
    position: absolute; top: 135px;
    width: 420px; height: 930px;
    border-radius: 18px; overflow: hidden;
    background: linear-gradient(160deg, var(--bg-top), var(--bg-bottom));
    font-family: "Quicksand", sans-serif;
  }
  .label--biotin { left: 95px; --bg-top: var(--blue-top); --bg-bottom: var(--blue-bottom); --ink: var(--blue-ink); --tint: var(--blue-tint); }
  .label--keratin { left: 555px; --bg-top: var(--pink-top); --bg-bottom: var(--pink-bottom); --ink: var(--pink-ink); --tint: var(--pink-tint); }

  .tagline {
    position: absolute; left: 10px; top: 50px; bottom: 50px; width: 34px;
    writing-mode: vertical-rl; transform: rotate(180deg);
    text-align: center;
    font-family: "Montserrat", sans-serif; font-weight: 300;
    font-size: 27px; letter-spacing: 6px; color: var(--tint);
    white-space: nowrap;
  }

  .brand-band {
    position: absolute; left: 58px; right: 0; top: 6px; height: 134px;
    background: linear-gradient(90deg, var(--gold-dark), var(--gold-light) 70%, var(--gold-dark));
    border-left: 4px solid var(--ink);
  }
  .brand-name {
    position: absolute; left: 12px; right: 8px; top: 30px;
    display: flex; justify-content: space-between;
    font-family: "Montserrat", sans-serif; font-weight: 700;
    font-size: 74px; line-height: 1; color: var(--white);
  }
  .brand-rule {
    position: absolute; left: 52px; right: 0; top: 152px; height: 4px;
    background: var(--gold-light);
  }
  .brand-bar {
    position: absolute; left: 52px; right: 0; top: 158px; height: 22px;
    background: var(--ink);
  }

  .count {
    position: absolute; left: 60px; top: 212px;
    font-family: "Oswald", sans-serif; font-weight: 300;
    font-size: 56px; line-height: 1; color: var(--ink);
  }
  .descriptor {
    position: absolute; left: 60px; top: 280px;
    font-family: "Oswald", sans-serif; font-weight: 300;
    font-size: 40px; line-height: 1; color: var(--white); letter-spacing: -1px;
  }
  .product-name {
    position: absolute; left: 57px; top: 322px;
    font-family: "Oswald", sans-serif; font-weight: 500;
    font-size: 118px; line-height: 1; color: var(--white); letter-spacing: -3px;
    transform: scaleX(0.72); transform-origin: left;
    white-space: nowrap;
  }
  .ingredient-tag {
    position: absolute; left: 58px; top: 447px;
    padding: 6px 22px 6px 8px;
    background: linear-gradient(90deg, var(--gold-dark), var(--gold-light));
    font-family: "Oswald", sans-serif; font-weight: 400;
    font-size: 20px; line-height: 1.15; color: var(--white);
  }

  .claims {
    position: absolute; left: 50px; right: 10px; top: 547px; height: 66px;
    background: var(--ink);
    display: flex; align-items: center; justify-content: space-between;
    padding: 0 8px;
  }
  .claim { display: flex; align-items: center; gap: 7px; }
  .claim svg { width: 30px; height: 30px; flex: none; }
  .claim-text {
    font-family: "Quicksand", sans-serif; font-weight: 600;
    font-size: 16px; line-height: 1.3; color: var(--tint);
    white-space: nowrap;
  }

  .benefits {
    position: absolute; left: 58px; top: 640px;
    display: grid; grid-template-columns: 128px 220px; row-gap: 9px;
    list-style: none;
  }
  .benefits li {
    position: relative; padding-left: 16px;
    font-size: 21px; line-height: 1.35; color: var(--ink);
    white-space: nowrap;
  }
  .benefits li::before {
    content: ""; position: absolute; left: 2px; top: 12px;
    width: 6px; height: 6px; border-radius: 50%; background: var(--gold-dot);
  }

  .volume {
    position: absolute; left: 50px; top: 858px;
    font-size: 22px; color: var(--white); font-weight: 500;
  }
</style>
</head>
<body>
<div class="canvas">

  <section class="label label--biotin">
    <div class="tagline">BRIGHTEN – REVIVE – EVERYDAY</div>
    <div class="brand-band"><div class="brand-name"><span>V</span><span>O</span><span>R</span><span>A</span></div></div>
    <div class="brand-rule"></div>
    <div class="brand-bar"></div>
    <div class="count">10-IN-1</div>
    <div class="descriptor">MULTI-USE LEAVE IN</div>
    <div class="product-name">LANE MIST</div>
    <div class="ingredient-tag">BIOTIN INFUSED FORMULA</div>
    <div class="claims">
      <div class="claim">
        <svg viewBox="0 0 32 32" aria-hidden="true"><circle cx="16" cy="16" r="14" fill="none" stroke="var(--tint)" stroke-width="1.5"/><rect x="9" y="11" width="10" height="6" rx="3" fill="none" stroke="var(--tint)" stroke-width="1.3"/><path d="M13 17v6M19 13h4" stroke="var(--tint)" stroke-width="1.3"/></svg>
        <span class="claim-text">Salon<br>Formula</span>
      </div>
      <div class="claim">
        <svg viewBox="0 0 32 32" aria-hidden="true"><circle cx="16" cy="16" r="14" fill="none" stroke="var(--tint)" stroke-width="1.5"/><ellipse cx="16" cy="16" rx="9" ry="4" fill="none" stroke="var(--tint)" stroke-width="1.2"/><ellipse cx="16" cy="16" rx="9" ry="4" transform="rotate(60 16 16)" fill="none" stroke="var(--tint)" stroke-width="1.2"/><ellipse cx="16" cy="16" rx="9" ry="4" transform="rotate(120 16 16)" fill="none" stroke="var(--tint)" stroke-width="1.2"/></svg>
        <span class="claim-text">Sulfate<br>Free</span>
      </div>
      <div class="claim">
        <svg viewBox="0 0 32 32" aria-hidden="true"><circle cx="16" cy="16" r="14" fill="none" stroke="var(--tint)" stroke-width="1.5"/><path d="M16 8v17M16 12l-4-2M16 12l4-2M16 16l-4-2M16 16l4-2M16 20l-4-2M16 20l4-2" stroke="var(--tint)" stroke-width="1.5" stroke-linecap="round"/></svg>
        <span class="claim-text">Paraben<br>Free</span>
      </div>
    </div>
    <ul class="benefits">
      <li>Moisturize</li><li>Split Ends</li>
      <li>Detangle</li><li>Frizz Control</li>
      <li>Breakage</li><li>Smooth Cuticle</li>
      <li>Shine</li><li>Strengthen Shine</li>
      <li>Hydrate</li><li>UV Protection</li>
    </ul>
    <div class="volume">10oz / 295mL</div>
  </section>

  <section class="label label--keratin">
    <div class="tagline">BRIGHTEN – REVIVE – EVERYDAY</div>
    <div class="brand-band"><div class="brand-name"><span>V</span><span>O</span><span>R</span><span>A</span></div></div>
    <div class="brand-rule"></div>
    <div class="brand-bar"></div>
    <div class="count">10-IN-1</div>
    <div class="descriptor">MULTI-USE LEAVE IN</div>
    <div class="product-name">LANE MIST</div>
    <div class="ingredient-tag">KERATIN INFUSED FORMULA</div>
    <div class="claims">
      <div class="claim">
        <svg viewBox="0 0 32 32" aria-hidden="true"><circle cx="16" cy="16" r="14" fill="none" stroke="var(--tint)" stroke-width="1.5"/><rect x="9" y="11" width="10" height="6" rx="3" fill="none" stroke="var(--tint)" stroke-width="1.3"/><path d="M13 17v6M19 13h4" stroke="var(--tint)" stroke-width="1.3"/></svg>
        <span class="claim-text">Salon<br>Formula</span>
      </div>
      <div class="claim">
        <svg viewBox="0 0 32 32" aria-hidden="true"><circle cx="16" cy="16" r="14" fill="none" stroke="var(--tint)" stroke-width="1.5"/><ellipse cx="16" cy="16" rx="9" ry="4" fill="none" stroke="var(--tint)" stroke-width="1.2"/><ellipse cx="16" cy="16" rx="9" ry="4" transform="rotate(60 16 16)" fill="none" stroke="var(--tint)" stroke-width="1.2"/><ellipse cx="16" cy="16" rx="9" ry="4" transform="rotate(120 16 16)" fill="none" stroke="var(--tint)" stroke-width="1.2"/></svg>
        <span class="claim-text">Sulfate<br>Free</span>
      </div>
      <div class="claim">
        <svg viewBox="0 0 32 32" aria-hidden="true"><circle cx="16" cy="16" r="14" fill="none" stroke="var(--tint)" stroke-width="1.5"/><path d="M16 8v17M16 12l-4-2M16 12l4-2M16 16l-4-2M16 16l4-2M16 20l-4-2M16 20l4-2" stroke="var(--tint)" stroke-width="1.5" stroke-linecap="round"/></svg>
        <span class="claim-text">Paraben<br>Free</span>
      </div>
    </div>
    <ul class="benefits">
      <li>Moisturize</li><li>Split Ends</li>
      <li>Detangle</li><li>Frizz Control</li>
      <li>Breakage</li><li>Smooth Cuticle</li>
      <li>Shine</li><li>Strengthen Shine</li>
      <li>Hydrate</li><li>UV Protection</li>
    </ul>
    <div class="volume">10oz / 295mL</div>
  </section>

</div>
</body>
</html>
```